Letterhead Design Project

Attached is our new Logo and a copy of our old letter head
Looking to rebrand with our new logo

Reason: I want to show a business card design

Industry/Entity Type

Film Production

Colors

Requirements
Must have
• The information on the old letterhead

```html
<!DOCTYPE html>
<html lang="en">
<head>
<meta charset="utf-8">
<title>Vantor International – Letterhead and Business Cards</title>
<link href="https://fonts.googleapis.com/css2?family=Oswald:wght@600&family=Roboto+Condensed:wght@400;700&display=swap" rel="stylesheet">
<style>
  :root{
    --backdrop:#5d8a9e;
    --paper:#ffffff;
    --navy:#0f4a6b;
    --blue:#1a86c8;
    --sky:#2aa6e0;
    --slate:#557488;
    --orange:#f07a1e;
    --ink:#111111;
    --shadow:rgba(0,0,0,.28);
  }
  *{margin:0;padding:0;box-sizing:border-box}
  html,body{width:1200px;height:1200px;overflow:hidden}
  body{background:var(--backdrop);position:relative;font-family:"Roboto Condensed",sans-serif}

  .letterhead{position:absolute;left:223px;top:69px;width:735px;height:1040px;background:var(--paper);overflow:hidden}
  .brand{position:absolute;display:flex;align-items:center;gap:8px;color:var(--blue);font-family:"Roboto Condensed",sans-serif;font-weight:700;line-height:1}
  .brand-dot{border-radius:50%;background:var(--blue);flex:none}
  .brand-name{display:flex;flex-direction:column}
  .letterhead .brand{left:28px;top:50px}
  .letterhead .brand-dot{width:30px;height:30px}
  .letterhead .brand-name .main{font-size:50px;letter-spacing:1px}
  .letterhead .brand-name .sub{font-size:15px;letter-spacing:3px;margin-top:4px}

  .contact{position:absolute;text-align:right;color:var(--slate);line-height:1.25;font-style:normal}
  .letterhead .contact{right:29px;top:30px;font-size:20.5px}

  .rule{position:absolute;height:2px;background:var(--orange)}
  .letterhead .rule{left:205px;right:29px;top:137px}

  .tagline{position:absolute;font-family:"Oswald",sans-serif;font-weight:600;color:var(--navy);white-space:nowrap;text-align:right}
  .tagline .amp{font-size:.72em}
  .tagline .hl{color:var(--blue)}
  .letterhead .tagline{right:29px;top:141px;font-size:18px;letter-spacing:.2px}

  .divisions{position:absolute;left:0;right:0;text-align:center;font-family:"Oswald",sans-serif;font-weight:600;color:var(--navy);white-space:nowrap}
  .divisions .dot{display:inline-block;border-radius:50%;background:var(--sky);vertical-align:middle}
  .letterhead .divisions{top:956px;font-size:16px}
  .letterhead .divisions .dot{width:9px;height:9px;margin:0 5px 3px 3px}
  .parent{position:absolute;left:0;right:0;text-align:center;color:var(--blue);white-space:nowrap}
  .letterhead .parent{top:983px;font-size:17px}
  .registry{position:absolute;left:0;right:0;text-align:center;color:var(--ink);font-weight:700;white-space:nowrap;word-spacing:2px}
  .letterhead .registry{top:1005px;font-size:16.5px}

  .card{position:absolute;width:311px;height:177px;background:var(--paper);box-shadow:4px 6px 12px var(--shadow);overflow:hidden}
  .card-front{left:549px;top:466px}
  .card-front .brand{left:0;right:0;top:52px;justify-content:center}
  .card-front .brand-dot{width:28px;height:28px}
  .card-front .brand-name .main{font-size:48px;letter-spacing:1px}
  .card-front .brand-name .sub{font-size:15px;letter-spacing:3px;margin-top:4px}

  .card-back{left:810px;top:600px}
  .card-back .brand{left:7px;top:12px;gap:5px}
  .card-back .brand-dot{width:13px;height:13px}
  .card-back .brand-name .main{font-size:24px;letter-spacing:.5px}
  .card-back .brand-name .sub{font-size:7.5px;letter-spacing:1.5px;margin-top:2px}
  .card-back .contact{right:7px;top:6px;font-size:10px;line-height:1.32}
  .card-back .holder{position:absolute;right:7px;top:70px;font-size:15px;line-height:1;color:var(--ink)}
  .card-back .rule{left:6px;right:7px;top:89px;height:1px}
  .card-back .tagline{left:6px;top:92px;font-size:10.4px;text-align:left}
  .card-back .divisions{top:120px;font-size:10.4px;line-height:1.25}
  .card-back .divisions .dot{width:6px;height:6px;margin:0 3px 2px 2px}
  .card-back .parent{top:147px;font-size:10px;color:var(--navy)}
  .card-back .registry{top:160px;font-size:9.5px}
</style>
</head>
<body>

<section class="letterhead" aria-label="Letterhead">
  <div class="brand">
    <span class="brand-dot"></span>
    <span class="brand-name"><span class="main">VANTOR</span><span class="sub">INTERNATIONAL</span></span>
  </div>
  <address class="contact">
    P.O. Box 418 Hillcrest QLD 4118<br>
    P.O. Box 372 Marlow NSW 2775<br>
    P.: 0400 555 019<br>
    E.: hello@vantor.example
  </address>
  <div class="rule"></div>
  <p class="tagline">SUPPLY <span class="amp">&amp;</span> <span class="hl">MANAGEMENT</span> OF <span class="hl">INFRASTRUCTURE</span> <span class="amp">&amp;</span> LOGISTICS</p>

  <p class="divisions">VANTOR FILM SERVICES<span class="dot"></span> VANTOR PILOT ESCORTS<span class="dot"></span> VANTOR TOUR MANAGEMENT <span class="dot"></span>VANTOR DRIVER</p>
  <p class="parent">ARE DIVISIONS OF VANTOR INTERNATIONAL PTY LTD</p>
  <p class="registry">ACN 000 482 116 &nbsp; ABN 00 000 482 116</p>
</section>

<section class="card card-front" aria-label="Business card front">
  <div class="brand">
    <span class="brand-dot"></span>
    <span class="brand-name"><span class="main">VANTOR</span><span class="sub">INTERNATIONAL</span></span>
  </div>
</section>

<section class="card card-back" aria-label="Business card back">
  <div class="brand">
    <span class="brand-dot"></span>
    <span class="brand-name"><span class="main">VANTOR</span><span class="sub">INTERNATIONAL</span></span>
  </div>
  <address class="contact">
    P.O. Box 418 Hillcrest QLD 4118<br>
    P.O. Box 372 Marlow NSW 2775<br>
    P.: 0400 555 019<br>
    E.: hello@vantor.example
  </address>
  <p class="holder">ALEX CARTER, OWNER</p>
  <div class="rule"></div>
  <p class="tagline">SUPPLY <span class="amp">&amp;</span> <span class="hl">MANAGEMENT</span> OF <span class="hl">INFRASTRUCTURE</span> <span class="amp">&amp;</span> LOGISTICS</p>
  <p class="divisions">VANTOR FILM SERVICES<span class="dot"></span> VANTOR PILOT ESCORTS<br>VANTOR TOUR MANAGEMENT<span class="dot"></span> VANTOR DRIVER</p>
  <p class="parent">ARE DIVISIONS OF VANTOR INTERNATIONAL PTY LTD</p>
  <p class="registry">ACN 000 482 116 &nbsp; ABN 00 000 482 116</p>
</section>

</body>
</html>
```